Business Card Design Project

Double sided business card - logo on one side, my details on the other.

I would like to see two options - my logo on a dark grey/black background and my logo on white.

My details as follows:

Trevin Howsam MBus, MRQT
P: 0471 520 164
E: trevin@trevinhowsam.com
W: www.trevinhowsam.com

Target Market(s)

Managers in business, universities and government.

Industry/Entity Type

Business

Requirements
Must have
• Quorvel, Mintaglo and Brastonet icons

```html
<!DOCTYPE html>
<html lang="en">
<head>
<meta charset="utf-8">
<title>Trevin Howsam — Business Card, Details Side</title>
<link href="https://fonts.googleapis.com/css2?family=Quicksand:wght@600;700&display=swap" rel="stylesheet">
<style>
  :root {
    --paper: #ffffff;
    --card: #221c1a;
    --ink-light: #ffffff;
    --mark: #1a1a1a;
    --social: #6f6c6b;
    --amber-1: #c9490a;
    --amber-2: #ef5a09;
    --amber-3: #f0780a;
    --amber-4: #f0980c;
    --amber-5: #ffaa33;
  }
  html, body {
    margin: 0;
    padding: 0;
    width: 766px;
    height: 1200px;
    overflow: hidden;
    background: var(--paper);
    font-family: "Quicksand", "Arial Rounded MT Bold", sans-serif;
  }
  .sheet {
    position: relative;
    width: 766px;
    height: 1200px;
  }
  .crop-marks {
    position: absolute;
    inset: 0;
  }
  .card {
    position: absolute;
    left: 94px;
    top: 93px;
    width: 578px;
    height: 1012px;
    background: var(--card);
    overflow: hidden;
  }
  .colour-band {
    position: absolute;
    left: 0;
    width: 100%;
    display: flex;
  }
  .colour-band span { flex: 1; }
  .colour-band span:nth-child(1) { background: var(--amber-1); }
  .colour-band span:nth-child(2) { background: var(--amber-2); }
  .colour-band span:nth-child(3) { background: var(--amber-3); }
  .colour-band span:nth-child(4) { background: var(--amber-4); }
  .colour-band span:nth-child(5) { background: var(--amber-5); }
  .top-band { top: 0; height: 21px; }
  .name-band { top: 408px; height: 57px; }
  .name-line {
    position: absolute;
    left: 60px;
    top: 408px;
    height: 57px;
    display: flex;
    align-items: center;
    gap: 8px;
    color: var(--ink-light);
    white-space: nowrap;
  }
  .person-name { font-size: 38px; font-weight: 700; letter-spacing: -0.3px; }
  .post-nominals { font-size: 24px; font-weight: 700; padding-top: 8px; }
  .contact {
    position: absolute;
    left: 0;
    width: 100%;
    text-align: center;
    color: var(--ink-light);
    font-weight: 700;
    margin: 0;
  }
  .contact-phone { top: 487px; font-size: 27px; letter-spacing: 2.5px; }
  .contact-email { top: 535px; font-size: 23px; letter-spacing: 1.8px; }
  .contact-web { top: 578px; font-size: 23px; letter-spacing: 2.6px; }
  .social-row {
    position: absolute;
    left: 0;
    top: 920px;
    width: 100%;
    height: 44px;
    display: flex;
    justify-content: center;
    align-items: center;
    gap: 22px;
  }
  .social-item {
    display: flex;
    align-items: center;
    gap: 7px;
    color: var(--social);
    font-size: 17px;
    font-weight: 700;
  }
  .social-square {
    width: 22px;
    height: 22px;
    border-radius: 4px;
    background: var(--social);
  }
</style>
</head>
<body>
<div class="sheet">
  <svg class="crop-marks" width="766" height="1200" viewBox="0 0 766 1200" aria-hidden="true">
    <g stroke="var(--mark)" stroke-width="1.5">
      <line x1="94" y1="0" x2="94" y2="56"/>
      <line x1="672" y1="0" x2="672" y2="56"/>
      <line x1="0" y1="93" x2="56" y2="93"/>
      <line x1="710" y1="93" x2="766" y2="93"/>
      <line x1="0" y1="1105" x2="56" y2="1105"/>
      <line x1="710" y1="1105" x2="766" y2="1105"/>
      <line x1="94" y1="1144" x2="94" y2="1200"/>
      <line x1="672" y1="1144" x2="672" y2="1200"/>
    </g>
  </svg>

  <div class="card">
    <div class="colour-band top-band"><span></span><span></span><span></span><span></span><span></span></div>
    <div class="colour-band name-band"><span></span><span></span><span></span><span></span><span></span></div>

    <div class="name-line">
      <span class="person-name">Trevin Howsam</span>
      <span class="post-nominals">MBus, MRQT</span>
    </div>

    <p class="contact contact-phone">0471 520 164</p>
    <p class="contact contact-email">trevin@trevinhowsam.com</p>
    <p class="contact contact-web">www.trevinhowsam.com</p>

    <div class="social-row">
      <div class="social-item"><span class="social-square"></span>Mintaglo</div>
      <div class="social-item"><span class="social-square"></span>Quorvel</div>
      <div class="social-item"><span class="social-square"></span>Brastonet</div>
    </div>
  </div>
</div>
</body>
</html>
```